Regional Consulting Business Needs a Business Card Design

We need a business card design for our new business based in Regional Victoria, Australia called Velor Power. We are a consulting company with our main goal being to save people momey money and reducing their carbon footprint. Anything from water saving showerheads, to energy saving lightglobes and even to solar power. We would like to see designs that use bright colours. The final design should shout 'we are here to help you'.

Industry/Entity Type

Business

```html
<!DOCTYPE html>
<html lang="en">
<head>
<meta charset="utf-8">
<title>Velor Power — Business Card</title>
<link rel="stylesheet" href="https://fonts.googleapis.com/css2?family=PT+Sans:wght@400;700&family=Arimo:wght@400;700&display=swap">
<style>
  :root {
    --backdrop: #b38a1f;
    --card: #ffffff;
    --accent: #f7b928;
    --ink: #1e1a14;
    --body: #333333;
    --muted: #6b6b6b;
  }
  * { box-sizing: border-box; margin: 0; padding: 0; }
  html, body { width: 1200px; height: 686px; overflow: hidden; }
  body { background: var(--backdrop); position: relative; font-family: "PT Sans", sans-serif; color: var(--ink); }

  .card { position: absolute; width: 524px; height: 299px; background: var(--card); box-shadow: 2px 2px 3px rgba(0,0,0,0.35); }
  .card--front { left: 60px; top: 136px; }
  .card--back { left: 609px; top: 288px; font-family: "Arimo", sans-serif; }

  /* Front */
  .rule { position: absolute; top: 118px; height: 2px; background: var(--accent); }
  .rule--left { left: 0; width: 28px; }
  .rule--mid { left: 291px; width: 173px; }
  .rule--right { left: 493px; width: 31px; }

  .brand { position: absolute; left: 38px; top: 100px; }
  .brand__row { display: flex; align-items: center; gap: 8px; }
  .brand__mark { width: 20px; height: 20px; background: var(--accent); }
  .brand__name { font-size: 26px; font-weight: 700; color: var(--ink); letter-spacing: 0.3px; line-height: 1; }
  .brand__tagline { margin-top: 6px; font-size: 9.5px; font-weight: 700; font-style: italic; color: var(--ink); }

  .person { position: absolute; right: 62px; top: 68px; text-align: right; }
  .person__name { font-size: 16px; font-weight: 700; color: var(--accent); line-height: 1.2; }
  .person__title { font-size: 12px; font-weight: 700; color: var(--ink); margin-top: 4px; }

  .contact { position: absolute; right: 60px; top: 138px; list-style: none; text-align: right; font-size: 12.5px; color: var(--ink); }
  .contact li { display: flex; justify-content: flex-end; align-items: center; gap: 5px; height: 19.3px; }
  .contact svg { width: 12px; height: 12px; flex: none; }
  .address { position: absolute; right: 76px; top: 219px; text-align: right; font-size: 12.5px; line-height: 16px; color: var(--ink); }

  /* Back */
  .package__title { position: absolute; left: 43px; top: 41px; font-size: 16.5px; font-weight: 700; color: var(--accent); }
  .package__list { position: absolute; left: 44px; top: 76px; width: 450px; list-style: none; font-size: 13px; line-height: 15.5px; color: var(--body); }
  .package__list li { position: relative; padding-left: 15px; margin-bottom: 15.5px; }
  .package__list li::before { content: ""; position: absolute; left: 2px; top: 3px; width: 7px; height: 7px; background: var(--accent); transform: rotate(45deg); }
</style>
</head>
<body>

<section class="card card--front" aria-label="Business card front">
  <div class="rule rule--left"></div>
  <div class="rule rule--mid"></div>
  <div class="rule rule--right"></div>

  <div class="brand">
    <div class="brand__row">
      <span class="brand__mark" aria-hidden="true"></span>
      <span class="brand__name">Velor Power</span>
    </div>
    <p class="brand__tagline">Maintanence and consulting services</p>
  </div>

  <div class="person">
    <p class="person__name">Your Name</p>
    <p class="person__title">Title</p>
  </div>

  <ul class="contact">
    <li>123-456-7890
      <svg viewBox="0 0 12 12" aria-hidden="true"><path d="M3 1l2 2.5-1.2 1.3a7 7 0 0 0 3.4 3.4L8.5 7 11 9l-1.3 2C5.5 11 1 6.5 1 2.3z" fill="var(--accent)"/></svg>
    </li>
    <li>123-456-7890
      <svg viewBox="0 0 12 12" aria-hidden="true"><rect x="3" y="1" width="6" height="4" fill="none" stroke="var(--accent)"/><rect x="1" y="5" width="10" height="6" fill="var(--accent)"/><rect x="3" y="7" width="6" height="1" fill="#fff"/><rect x="3" y="9" width="6" height="1" fill="#fff"/></svg>
    </li>
    <li>name@website.com
      <svg viewBox="0 0 12 12" aria-hidden="true"><rect x="0.5" y="2.5" width="11" height="7.5" fill="var(--accent)"/><path d="M0.5 2.5L6 7l5.5-4.5" fill="none" stroke="#fff" stroke-width="1"/></svg>
    </li>
    <li>www.website.com
      <svg viewBox="0 0 12 12" aria-hidden="true"><circle cx="6" cy="6" r="5" fill="var(--accent)"/><ellipse cx="6" cy="6" rx="2.2" ry="5" fill="none" stroke="#fff" stroke-width="0.8"/><path d="M1 6h10M2 3.5h8M2 8.5h8" stroke="#fff" stroke-width="0.8"/></svg>
    </li>
  </ul>

  <p class="address">Street name<br>City, State, zip code</p>
</section>

<section class="card card--back" aria-label="Business card back">
  <h2 class="package__title">Product Package</h2>
  <ul class="package__list">
    <li>Free energy assessment of your home or business</li>
    <li>Free advice on energy and water sustainability</li>
    <li>Free gas and solar hot water rebate eligibility assessment</li>
    <li>Free solar power rebate eligibility assessment</li>
    <li>We offer rebates of up to $2000 for the purchase and implementation of a range of eligible water reduction and sustainability products appliances and services.</li>
  </ul>
</section>

</body>
</html>
```